Cat-products company needs smart, yet endearing, business card

We need a business card design for a new, but up-and-running, business based in Honolulu, Hawaii. The business is Purrlane Nest Co. Our first product is the most environmentally-friendly cat grass kit ever seen on the planet. Future products, currently in the R&D phase, will include a variety of exciting cat scratchers. We also do consulting work to help apartment-dwellers make their home more cat-friendly and, in the future, plan on doing full, custom installs of structure to create high walkways for cats.

Target Market(s)

Middle-aged, apartment-dwelling, middle-class workers who own 1 or more cats and who dote on them.

Industry/Entity Type

Pet Care

Contact Information for Business Card

A striking, professional, yet warm and friendly design is what we're after.

Font styles to use
Serif
Sans Serif
Other font styles liked:
• Comfortaa

Colors

Designer to choose colors to be used in the design.

Requirements
Must have
• The company logo: (see attachment)
• The company name: Purrlane Nest Co
• The web address: www.purrlanenestco.example
• Email: support@purrlanenestco.example
• Phone: +1 (808) 574 1630
• Update (Fri Jun 30 3017 7:45pm Hawaii Time) I would like, is possible, uploaded picture of the cat grass kit on the back of the card with some text along the lines of: Purrlane Nest Co - Maker Of The Freshest Cat Grass Kit Yet
Nice to have
• A cat picture, cartoon, real or silhouette that illustrates cats in action and/or relaxing; ie using the apartment space to live, play and relax in and being well-contented.
• Most of the website is done in the font: Comfortaa. It might be nice to continue using this for brand consistency.
Should not have
• Hard-to-read fonts.

```html
<!DOCTYPE html>
<html lang="en">
<head>
<meta charset="utf-8">
<title>Purrlane Nest Co — Business Card</title>
<link href="https://fonts.googleapis.com/css2?family=Montserrat:wght@400;700&family=Tinos:wght@700&display=swap" rel="stylesheet">
<style>
  :root {
    --backdrop: #bcbdbf;
    --card: #ffffff;
    --ink: #111111;
    --brown: #4e3129;
    --orange: #f5a81c;
    --grass-dark: #3f6a1e;
    --grass-mid: #5f8f2a;
    --grass-light: #b8d83c;
  }
  * { margin: 0; padding: 0; box-sizing: border-box; }
  html, body {
    width: 1200px; height: 927px; overflow: hidden;
    background: var(--backdrop);
    font-family: "Montserrat", sans-serif;
  }
  .card {
    position: absolute; left: 262px; width: 659px; height: 376px;
    border-radius: 14px; overflow: hidden;
    box-shadow: 6px 8px 10px rgba(0,0,0,0.35);
  }
  .card--front { top: 69px; background: var(--card); }
  .card--back { top: 482px; }

  .brand {
    position: absolute; left: 0; width: 268px; top: 120px;
    display: flex; flex-direction: column; align-items: center; gap: 14px;
  }
  .brand__dot { width: 58px; height: 58px; border-radius: 50%; background: var(--brown); }
  .brand__name { font-weight: 700; font-size: 21px; color: var(--orange); white-space: nowrap; }

  .divider {
    position: absolute; left: 268px; top: 118px; width: 1.5px; height: 155px;
    background: var(--brown);
  }
  .company {
    position: absolute; left: 326px; top: 168px;
    font-family: "Tinos", serif; font-weight: 700; font-size: 25px; color: var(--ink);
  }
  .contacts {
    position: absolute; left: 326px; top: 192px; list-style: none;
    font-size: 17px; color: var(--ink); line-height: 22px;
  }
  .contacts li { display: flex; align-items: center; }
  .contacts svg { width: 13px; height: 13px; margin-right: 16px; flex: none; }
  .accent { color: var(--orange); }

  .photo {
    position: absolute; inset: 0;
    background:
      radial-gradient(ellipse 40% 35% at 78% 8%, var(--grass-light), transparent 70%),
      linear-gradient(180deg, var(--grass-mid) 0%, var(--grass-dark) 100%);
  }
  .back__name {
    position: absolute; left: 0; right: 0; top: 254px; text-align: center;
    font-weight: 700; font-size: 26px; color: var(--ink);
  }
  .back__tagline {
    position: absolute; left: 0; right: 0; top: 330px; text-align: center;
    font-size: 16px; color: var(--ink);
  }
</style>
</head>
<body>
  <section class="card card--front">
    <div class="brand">
      <span class="brand__dot"></span>
      <span class="brand__name">Purrlane Nest Co</span>
    </div>
    <div class="divider"></div>
    <h1 class="company">Purrlane Nest Co</h1>
    <ul class="contacts">
      <li>
        <svg viewBox="0 0 16 16" aria-hidden="true"><path d="M4 1.5 L6.5 5 L5 6.5 Q6.5 9.5 9.5 11 L11 9.5 L14.5 12 L12.5 14.5 Q5 14 1.5 3.5 Z" fill="none" stroke="#f5a81c" stroke-width="1.4" stroke-linejoin="round"/></svg>
        www.purrlanenestco.example
      </li>
      <li>
        <svg viewBox="0 0 16 16" aria-hidden="true"><rect x="1.5" y="3.5" width="13" height="9" fill="none" stroke="#f5a81c" stroke-width="1.4"/><path d="M1.5 3.5 L8 9 L14.5 3.5" fill="none" stroke="#f5a81c" stroke-width="1.4"/></svg>
        <span>support@<span class="accent">purrlanenestco</span>.example</span>
      </li>
      <li>
        <svg viewBox="0 0 16 16" aria-hidden="true"><circle cx="8" cy="8" r="6.5" fill="none" stroke="#f5a81c" stroke-width="1.3"/><ellipse cx="8" cy="8" rx="3" ry="6.5" fill="none" stroke="#f5a81c" stroke-width="1.1"/><path d="M1.5 8 H14.5 M2.5 5 H13.5 M2.5 11 H13.5" stroke="#f5a81c" stroke-width="1"/></svg>
        +1 (808) 574 1630
      </li>
    </ul>
  </section>

  <section class="card card--back">
    <div class="photo" role="img" aria-label="Photo of a fluffy grey and white cat lying on green grass"></div>
    <p class="back__name">Purrlane Nest Co</p>
    <p class="back__tagline">Maker Of The Freshest Cat Grass Kit Yet</p>
  </section>
</body>
</html>
```